Retirement Plan Advisor Bio

See the attached document and photo for content. I would like someone to design this one page flyer using my logo. This logo was designed by a designer with sketch hive. I am looking for a professional looking document. I want to he color scheme to be primarily white and gold.

Target Market(s)

Employers who offer a retirement plan

Requirements
Should not have
• The designs that I have received look more like resumes. I am interested in advertising my Retirement plan services. If anyone can change their submissions and change it to an ad for retirement plan services instead of a Bio or resume, I would prefer that.

```html
<!DOCTYPE html>
<html lang="en">
<head>
<meta charset="utf-8">
<title>Financial Planning Services – Helen R Marsh</title>
<link href="https://fonts.googleapis.com/css2?family=Montserrat:wght@500;600;700&family=Raleway:wght@300;400;500&family=Arimo:wght@400;700&display=swap" rel="stylesheet">
<style>
:root{
  --gold:#a98a58;
  --gold-light:#c9a86a;
  --gold-dark:#7a5f33;
  --brown-band:#3a3028;
  --card:rgba(92,76,56,.93);
  --white:#ffffff;
  --ink:#3a3028;
}
*{margin:0;padding:0;box-sizing:border-box}
html,body{width:928px;height:1200px;overflow:hidden;background:var(--white)}
.flyer{position:relative;width:928px;height:1200px;overflow:hidden;background:var(--white);font-family:"Raleway",sans-serif}
.hero{position:absolute;left:0;top:0;width:928px;height:640px;
  background:radial-gradient(circle at 18% 38%,#f6d48a 0%,#e9a94a 14%,#a58a3e 32%,transparent 55%),
  linear-gradient(180deg,#8aa05a 0%,#6e8a45 40%,#9d9a6a 70%,#c9c0a8 100%)}
.hero-swoosh{position:absolute;left:0;top:0}
.brand{position:absolute;left:20px;top:62px;display:flex;align-items:center;gap:10px}
.brand-mark{width:30px;height:30px;background:var(--gold)}
.brand-name{font-family:"Raleway",sans-serif;font-weight:400;font-size:27px;color:var(--gold);letter-spacing:.5px}
.services-band{position:absolute;left:0;top:421px;width:488px;height:46px;background:var(--brown-band);
  color:var(--white);font-family:"Montserrat",sans-serif;font-weight:700;font-size:26px;line-height:46px;padding-left:41px}
.lower-curve{position:absolute;left:0;top:540px}
.card{position:absolute;top:479px;width:272px;height:248px;background:var(--card);border-radius:4px;
  border-bottom:3px solid #3e3226;padding:28px 20px 0 20px;color:var(--white)}
.card h3{font-family:"Montserrat",sans-serif;font-weight:600;font-size:16px;line-height:22px;letter-spacing:.3px;margin-bottom:18px}
.card p{font-family:"Raleway",sans-serif;font-weight:400;font-size:13px;line-height:16.3px}
.card--one{left:40px}.card--two{left:339px}.card--three{left:634px}
.portrait{position:absolute;left:49px;top:751px;width:252px;height:324px;
  background:linear-gradient(180deg,#6d7e9a 0%,#8896ae 45%,#4a4f5c 100%)}
.portrait-rule{position:absolute;left:49px;top:1082px;width:244px;height:2px;background:var(--gold)}
.advisor-name{position:absolute;left:51px;top:1088px;font-family:"Montserrat",sans-serif;font-weight:600;font-size:21px;line-height:25px;color:var(--gold);letter-spacing:.3px}
.advisor-name sup{font-size:10px}
.timeline{position:absolute;left:323px;top:760px;width:585px}
.timeline-line{position:absolute;left:11px;top:12px;width:2px;height:290px;background:var(--gold)}
.entry{position:absolute;left:0;width:585px}
.entry-dot{position:absolute;left:0;top:0;width:24px;height:24px;border-radius:50%;border:5px solid var(--gold);background:var(--white)}
.entry-body{margin-left:37px;font-family:"Arimo",sans-serif;color:var(--gold)}
.entry-title{font-weight:700;font-size:15px;line-height:20px;margin-bottom:8px}
.entry-lead{font-size:13.4px;line-height:15px}
.entry-text{font-size:11px;line-height:15px}
.entry-list li{list-style:none;font-size:11.2px;line-height:18.7px}
.degree{font-weight:700;font-size:11.8px;margin-bottom:5px}
.entry--intro{top:0}.entry--spec{top:78px}.entry--qual{top:163px}.entry--edu{top:289px}
.footer{position:absolute;left:0;top:1161px;width:928px;height:39px;background:var(--brown-band);color:var(--white);
  font-family:"Arimo",sans-serif;font-size:14.5px;line-height:39px;text-align:center}
</style>
</head>
<body>
<div class="flyer">
  <div class="hero" role="img" aria-label="Photo of a smiling multi-generation family holding small flags outdoors at sunset"></div>

  <svg class="hero-swoosh" width="928" height="230" viewBox="0 0 928 230">
    <path d="M0 0 H420 C400 110 300 190 0 200 Z" fill="#ffffff"/>
    <path d="M0 196 C260 195 380 150 425 0" fill="none" stroke="#b08f55" stroke-width="3"/>
    <path d="M0 214 C120 206 220 206 280 190" fill="none" stroke="#8a6a38" stroke-width="4"/>
  </svg>
  <div class="brand"><span class="brand-mark"></span><span class="brand-name">Verity Financial, LLC</span></div>

  <svg class="lower-curve" width="928" height="100" viewBox="0 0 928 100">
    <path d="M0 100 V80 C300 20 620 20 928 80 V100 Z" fill="#ffffff"/>
    <path d="M0 78 C300 18 620 18 928 78" fill="none" stroke="#b08f55" stroke-width="3"/>
  </svg>

  <div class="services-band">Financial Planning Services</div>

  <section class="card card--one">
    <h3>RETIREMENT PLANNING</h3>
    <p>My strategies help you assemble the pieces of this puzzle into an plan. Your vision can be pursued.</p>
  </section>
  <section class="card card--two">
    <h3>INVESTMENT<br>MANAGEMENT</h3>
    <p>Assessing your risk level and matching it up with a portfolio of investments is key to building your nest egg as well as making it last. My job is to help you live out your retirement years with a sense of financial independence.</p>
  </section>
  <section class="card card--three">
    <h3>RETIREMENT PLAN<br>DEVELOPMENT</h3>
    <p>Designing a plan that will benefit, both, the employees as well as the employer, choosing a lineup of world class investments, keeping cost down and keeping up with industry regulation all play a part in improving participant outcome. My experience brings experience in all these areas.</p>
  </section>

  <div class="portrait" role="img" aria-label="Portrait photo of the advisor"></div>
  <div class="portrait-rule"></div>
  <div class="advisor-name">Helen R Marsh CWP<sup>®</sup>APF<sup>®</sup><br>Northgate Advisor</div>

  <div class="timeline">
    <div class="timeline-line"></div>
    <div class="entry entry--intro">
      <span class="entry-dot"></span>
      <div class="entry-body"><p class="entry-lead">Over 18 years of experience in the retirement plan industry Focused on helping plan sponsors reduce administrative burdens and fiduciary risk Dedicated to helping employees work toward a positive retirement outcome through careful analysis of their savings rate, investment strategy and overall financial&nbsp; wellness</p></div>
    </div>
    <div class="entry entry--spec">
      <span class="entry-dot"></span>
      <div class="entry-body">
        <h4 class="entry-title">PROFESSIONAL SPECIALTIES</h4>
        <p class="entry-text">I strive to improve retirement outcomes for my plan sponsor clients and their<br>employees through careful retirement plan design assistance, strategic and<br>targeted communication and education , as well as continual monitoring of results.</p>
      </div>
    </div>
    <div class="entry entry--qual">
      <span class="entry-dot"></span>
      <div class="entry-body">
        <h4 class="entry-title">QUALIFICATIONS</h4>
        <ul class="entry-list">
          <li>Certified Wealth Planner®</li>
          <li>Accredited Plan Fiduciary®</li>
          <li>Investment Advisor Representative</li>
          <li>Series 7, 63, and 65 Securities licenses with Northgate Securities</li>
          <li>Holds Life and Health Insurance licenses from Illinois</li>
        </ul>
      </div>
    </div>
    <div class="entry entry--edu">
      <span class="entry-dot"></span>
      <div class="entry-body">
        <h4 class="entry-title">EDUCATION</h4>
        <p class="degree">BS Westbrook University, 1987</p>
        <p class="entry-text">*Securities and Investment Advisory Services offered through<br>Northgate Securities Group, Inc, a Registered Broker/Dealer and Investment Advisor, member NSRB/ISPF</p>
      </div>
    </div>
  </div>

  <footer class="footer">2400 Alder Rd. | Lakeview, IL 60999 | (555)210.4477 | helen.marsh@northgate.example | www.helenmarsh.example</footer>
</div>
</body>
</html>
```